serious, thorough, light and simple - that's my advice and mediations

My business card should combine my logo (uploaded file) and my homepage (https://fellor-mediation.webnestsite.com).

Contact Information for Business Card

Name: Sabine Fellor di Vanti
Phone: 076 412 58 94
mail: sfellor@postkiv.ch
web: www.fellor-di-vanti.ch

```html
<!DOCTYPE html>
<html lang="de">
<head>
<meta charset="utf-8">
<title>Visitenkarte – Sabine Fellor di Vanti</title>
<link rel="stylesheet" href="https://fonts.googleapis.com/css2?family=Lato:wght@400&family=Roboto:wght@400&display=swap">
<style>
  :root {
    --paper: #ffffff;
    --ink: #140b0e;
    --band: #6e3649;
    --band-text: #ffffff;
    --brand-gold: #a8874f;
    --brand-green: #1d6b3e;
  }
  * { margin: 0; padding: 0; box-sizing: border-box; }
  html, body { width: 1200px; height: 686px; overflow: hidden; background: var(--paper); }
  .card { position: relative; width: 1200px; height: 686px; background: var(--paper); overflow: hidden; }

  .brand {
    position: absolute; left: 140px; top: 168px;
    display: flex; align-items: center; gap: 16px;
  }
  .brand-dot { width: 34px; height: 34px; border-radius: 50%; background: var(--brand-green); }
  .brand-name {
    font-family: "Lato", sans-serif; font-weight: 400;
    font-size: 42px; color: var(--brand-gold); letter-spacing: 0.5px;
  }

  .holder { position: absolute; left: 564px; top: 122px; width: 538px; }
  .holder-name {
    font-family: "Lato", sans-serif; font-weight: 400;
    font-size: 61px; line-height: 72px; color: var(--ink); white-space: nowrap;
  }
  .holder-rule { margin-top: 2px; height: 2.5px; background: var(--ink); }

  .contact-band { position: absolute; left: 0; top: 413px; width: 1200px; height: 273px; background: var(--band); }
  .contact-list { position: absolute; left: 80px; top: 65px; list-style: none; }
  .contact-item {
    display: flex; align-items: center; height: 49px;
    font-family: "Roboto", sans-serif; font-size: 37px; color: var(--band-text);
  }
  .contact-icon { width: 30px; height: 30px; margin-right: 27px; flex: none; }
  .contact-rule { position: absolute; left: 80px; top: 219px; width: 1034px; height: 2px; background: var(--band-text); }
</style>
</head>
<body>
<div class="card">
  <div class="brand">
    <span class="brand-dot"></span>
    <span class="brand-name">Wege im Dialog</span>
  </div>

  <div class="holder">
    <div class="holder-name">Sabine Fellor di Vanti</div>
    <div class="holder-rule"></div>
  </div>

  <div class="contact-band">
    <ul class="contact-list">
      <li class="contact-item">
        <svg class="contact-icon" viewBox="0 0 30 30" aria-hidden="true">
          <path d="M7 3c1.5-.6 2.5.2 3.2 1.6l1.6 3.6c.5 1.2 0 2-1 2.7l-1.2.8c1 3.4 3.5 6.5 6.6 8.2l1-1c.9-.9 1.8-1 2.8-.3l3 2.2c1.1.8 1.2 1.9.3 3l-1.2 1.4C20.5 27 18 27 15 25 9 21 4.8 14.4 4.4 8 4.3 5.5 5.4 3.8 7 3z" fill="#fff"/>
          <path d="M16 6a6 6 0 0 1 6 6M16 9.5a2.7 2.7 0 0 1 2.6 2.6M16 2.5a9.5 9.5 0 0 1 9.5 9.5" fill="none" stroke="#fff" stroke-width="1.3" stroke-linecap="round"/>
        </svg>
        <span>+076 412 58 94</span>
      </li>
      <li class="contact-item">
        <svg class="contact-icon" viewBox="0 0 30 30" aria-hidden="true">
          <rect x="0" y="5" width="30" height="22" rx="2" fill="#fff"/>
          <path d="M1.5 7.5 15 18 28.5 7.5" fill="none" stroke="var(--band)" stroke-width="1.6"/>
        </svg>
        <span>sfellor@postkiv.ch</span>
      </li>
      <li class="contact-item">
        <svg class="contact-icon" viewBox="0 0 30 30" aria-hidden="true">
          <g fill="none" stroke="#fff" stroke-width="2">
            <circle cx="15" cy="15" r="13"/>
            <ellipse cx="15" cy="15" rx="6" ry="13"/>
            <path d="M15 2v26M2 15h26M4 8.5h22M4 21.5h22"/>
          </g>
        </svg>
        <span>www.fellor-di-vanti.ch</span>
      </li>
    </ul>
    <div class="contact-rule"></div>
  </div>
</div>
</body>
</html>
```